Redesign of my Homepage - Online resource for anyone to learn American Sign Language

I would like to have a new homepage design http://www.HandwiseLessons.example . My business is a website for anyone to learn American Sign Language. There are over 300 video lessons, with each lesson having 20 vocabulary words, retention exercises, 16,000 video dictionary etc. It is a very extensive site. It is a self paced website. If you need a log in to see what customers see, please let me know. I would like to keep the same color scheme. I want the website to look modern and clean. I want a fresh look! I want something that is easy to navigate, attracts customers, and easy to follow. I would like the final design to communicate that my website is for anyone to learn how to sign with this incredible program.

Target Market(s)

Students taking American Sign Language, Parents with Deaf children, future interpreters for the deaf, co-workers of the Deaf. Also, schools that offer American Sign Language (online schools, homeschools, etc. ).

Industry/Entity Type

Business

Number of Pages Required

1 page

Requirements
Must have
• My project must be very clean and clear. I want my homepage to show that this is a program for people to learn how American Sign Language.
Nice to have
• Not sure. Surprise me.

```html
<!DOCTYPE html>
<html lang="en">
<head>
<meta charset="utf-8">
<title>HandwiseLessons – Learn ASL Online</title>
<link rel="stylesheet" href="https://fonts.googleapis.com/css2?family=Arimo:wght@400;700&display=swap">
<style>
:root{
  --navy:#1d3266;
  --navy-dark:#16264f;
  --green:#2db53c;
  --blue:#2a5db0;
  --red:#c4141e;
  --purple:#5b2a8c;
  --ink:#222;
  --muted:#666;
  --light:#eef2f7;
  --white:#fff;
}
*{box-sizing:border-box;margin:0;padding:0}
html,body{width:1200px;height:3896px;overflow:hidden}
body{font-family:"Arimo",Arial,sans-serif;color:var(--ink);background:var(--white);position:relative}
.abs{position:absolute}
a{color:inherit;text-decoration:none}

/* top bar */
.topbar{left:0;top:0;width:1200px;height:26px;background:var(--navy);color:#fff;font-size:11px;display:flex;align-items:center;padding:0 160px;justify-content:space-between}
.topbar span{margin-right:18px}
/* header */
.header{left:0;top:26px;width:1200px;height:91px;display:flex;align-items:center;padding:0 160px;justify-content:space-between}
.brand{display:flex;align-items:center;gap:10px;font-size:30px;font-weight:700;color:var(--navy)}
.brand i{width:14px;height:14px;background:var(--green);border-radius:50%;display:block}
.welcome{color:var(--green);font-weight:700;font-size:17px}
/* nav */
.nav{left:0;top:117px;width:1200px;height:43px;background:var(--navy);display:flex;align-items:center;padding:0 160px;gap:28px;color:#fff;font-size:11px;font-weight:700;text-transform:uppercase}
.nav .on{color:var(--green)}
/* hero */
.hero{left:0;top:160px;width:1200px;height:578px;background:linear-gradient(120deg,#6c6f78 0%,#c7a68c 40%,#e0c9b4 60%,#4f6a86 100%)}
.hero-copy{left:160px;top:298px}
.hero-copy div{background:rgba(20,20,30,.75);color:#fff;font-weight:700;display:inline-block;padding:8px 12px;margin-bottom:22px}
.h1{font-size:36px}
.h2{font-size:22px}
.h3{font-size:18px}
.arrow{top:420px}
.dots{left:555px;top:686px;display:flex;gap:10px}
.dots span{width:20px;height:20px;border-radius:50%;background:#fff}
.dots span.on{background:var(--green);border:3px solid #fff}
/* trial */
.trial{left:0;top:738px;width:1200px;height:246px;background:var(--navy)}
.trial h2{position:absolute;left:160px;top:96px;color:#fff;font-size:32px}
.trial .btn{position:absolute;left:793px;top:832px}
.btn{border:2px solid #fff;color:#fff;font-weight:700;font-size:16px;width:246px;height:58px;display:flex;align-items:center;justify-content:center}
/* features card */
.card{left:155px;top:984px;width:886px;height:656px;border:1px solid #ccc;background:#fff}
.stat{left:528px;top:875px;width:190px;height:190px;transform:rotate(45deg);background:#fff;box-shadow:0 2px 6px rgba(0,0,0,.15)}
.stat-text{left:528px;top:955px;width:190px;text-align:center}
.stat-text b{display:block;color:var(--green);font-size:34px}
.stat-text span{color:var(--muted);font-size:20px;font-weight:700}
.sec-title{color:var(--green);font-weight:700;font-size:26px;text-align:center;width:1200px;left:0}
.lede{font-size:10px;font-weight:700;line-height:16px;text-align:center}
.feat{width:200px;text-align:center}
.feat .circ{position:absolute;left:0;top:0;width:200px;height:200px;border-radius:50%;background:#e8eef6;top:60px}
.feat .dia{position:relative;margin:0 auto;width:62px;height:62px;background:var(--blue);transform:rotate(45deg);display:flex;align-items:center;justify-content:center}
.feat .dia svg{transform:rotate(-45deg)}
.feat h3{position:relative;margin-top:30px;font-size:22px;color:#333}
.feat p{position:relative;font-size:9px;line-height:15px;font-weight:700;margin-top:10px;padding:0 30px;text-align:left}
/* course cards */
.course{width:372px;height:427px;border:1px solid #ccc;background:#fff}
.course .tab{height:57px;display:flex;align-items:center;justify-content:center;gap:10px;font-size:26px;font-weight:700}
.course .photo{height:233px}
.course .band{height:137px;color:#fff;padding:14px 16px}
.course .band b{display:block;font-size:12px;text-transform:uppercase;margin-bottom:8px}
.course .band p{font-size:9px;line-height:14px;font-weight:700}
/* articles / faq */
.col-title{font-size:28px;color:#333}
.art-num{font-size:32px;color:var(--green)}
.art-head{font-size:20px}
.small{font-size:10px;line-height:16px}
.pager{display:flex;gap:12px}
.pager span{width:24px;height:24px;border-radius:50%;background:#ddd;font-size:11px;display:flex;align-items:center;justify-content:center}
.pager span.on{background:var(--green)}
.faq{width:597px}
.faq .q{display:flex;justify-content:space-between;font-size:19px;padding:6px 0;border-bottom:1px solid #ddd}
.faq .q.open{color:var(--blue)}
.faq .q b{font-size:26px;line-height:18px;color:#333}
/* experts */
.experts{left:435px;top:2668px;width:765px;height:829px;background:linear-gradient(135deg,#2e4a93,#1d3266 70%,#2a4486)}
.experts h4{position:absolute;left:0;width:765px;text-align:center;top:34px;color:#fff;font-size:13px}
.expert{width:225px;background:#fff}
.expert .pic{height:285px}
.expert .name{height:32px;color:var(--green);font-size:11px;font-weight:700;display:flex;align-items:center;justify-content:center}
.founder{left:0;top:2824px;width:435px;height:673px;background:var(--light)}
.founder .pic{position:absolute;left:28px;top:60px;width:220px;height:200px;background:var(--navy);border:4px solid #fff;outline:1px solid #999}
/* footer */
.footer{left:0;top:3497px;width:1200px;height:264px;background:var(--light)}
.fcol h5{font-size:11px;font-weight:700;margin-bottom:8px;text-transform:uppercase}
.fcol li{list-style:none;font-size:13px;line-height:20px;color:#444}
.fcol li::before{content:"›";color:var(--green);margin-right:6px;font-weight:700}
.signup{display:flex;width:300px;height:34px;border:1px solid #bbb;background:#fff}
.signup span{flex:1;font-size:12px;color:#999;padding:9px 10px}
.signup i{width:40px;background:var(--green);display:flex;align-items:center;justify-content:center}
.socials{display:flex;gap:8px}
.socials span{width:30px;height:30px;border-radius:50%;background:#b8c0cc}
.copy{left:0;top:3761px;width:1200px;height:135px;background:var(--navy);color:#fff;font-size:13px;font-weight:700;display:flex;align-items:center;justify-content:center}
</style>
</head>
<body>

<div class="abs topbar"><div><span>☎ (555) 010 2468</span><span>✉ hello@handwiselessons.example</span></div><div><span>Login</span><span>Register</span></div></div>

<header class="abs header">
  <div class="brand"><i></i>Handwise</div>
  <div class="welcome">WELCOME TO ASL LEARN THROUGH VIDEO LESSONS ONLINE</div>
</header>

<nav class="abs nav">
  <a class="on">Home</a><a>About us ▾</a><a>Course plan ▾</a><a>Buy now</a><a>Testimonial</a><a>Group rate form</a><a>Teacher's guide</a><a>Contact us ▾</a>
</nav>

<section class="abs hero" role="img" aria-label="Photo of a mother and young daughter practising sign language at home"></section>
<div class="abs hero-copy">
  <div class="h1">Learn ASL from home in your own time</div><br>
  <div class="h2">Breakdown the block unfold your feelings</div><br>
  <div class="h3">Online tools ans resources</div>
</div>
<svg class="abs arrow" style="left:14px" width="30" height="70"><polyline points="26,2 4,35 26,68" fill="none" stroke="#fff" stroke-width="3"/></svg>
<svg class="abs arrow" style="left:1140px" width="30" height="70"><polyline points="4,2 26,35 4,68" fill="none" stroke="#fff" stroke-width="3"/></svg>
<div class="abs dots"><span></span><span></span><span class="on"></span></div>

<section class="abs trial"><h2>TRY FREE TRIAL</h2></section>
<a class="abs btn" style="left:793px;top:832px">START NOW</a>

<section class="abs card"></section>
<div class="abs stat"></div>
<div class="abs stat-text"><b>10,000+</b><span>Videos</span></div>

<h2 class="abs sec-title" style="top:1140px">OUR KEY FEATURES</h2>
<p class="abs lede" style="left:220px;top:1184px;width:760px">Learn every sign at your own pace with short video lessons, clear practice drills and a growing video dictionary. Each lesson adds new vocabulary, review games and retention exercises so progress feels steady and simple.</p>

<div class="abs feat" style="left:206px;top:1285px"><div class="circ"></div>
  <div class="dia"><svg width="30" height="30"><path d="M6 22c2-8 6-12 12-14M12 24c4-4 8-6 14-6" stroke="#fff" stroke-width="3" fill="none" stroke-linecap="round"/></svg></div>
  <h3>LEARN ASL</h3><p>Start with the alphabet and everyday words, then build full phrases through guided video lessons and quick quizzes.</p></div>
<div class="abs feat" style="left:501px;top:1285px"><div class="circ"></div>
  <div class="dia"><svg width="30" height="30"><circle cx="10" cy="9" r="4" fill="#fff"/><circle cx="21" cy="9" r="4" fill="#fff"/><rect x="6" y="15" width="8" height="10" fill="#fff"/><rect x="17" y="15" width="8" height="10" fill="#fff"/></svg></div>
  <h3>USING ASL</h3><p>Practise real conversations for home, school and work with scenes that show how signs are used in daily life.</p></div>
<div class="abs feat" style="left:796px;top:1285px"><div class="circ"></div>
  <div class="dia"><svg width="30" height="30"><circle cx="15" cy="8" r="5" fill="#fff"/><path d="M6 27c0-8 4-12 9-12s9 4 9 12z" fill="#fff"/></svg></div>
  <h3>TUTOR ONLINE</h3><p>Book time with a tutor for feedback on your signing, extra help with tricky words and tips for fluent conversation.</p></div>

<h2 class="abs sec-title" style="top:1690px">CHOOSE THE COURSE &nbsp;YOU WANT TO LEARN</h2>
<p class="abs lede" style="left:220px;top:1730px;width:760px">Pick the path that fits you best. Every course shares the same lesson library, with extra guidance shaped around students, families and the wider community of signers.</p>

<div class="abs course" style="left:0;top:1821px">
  <div class="tab" style="color:var(--red)"><svg width="30" height="30"><circle cx="15" cy="10" r="6" fill="none" stroke="#999" stroke-width="2"/><path d="M4 28c0-8 5-11 11-11s11 3 11 11" fill="none" stroke="#999" stroke-width="2"/></svg>Students</div>
  <div class="photo" role="img" aria-label="Photo of a student raising her hand in class" style="background:linear-gradient(135deg,#d9d6d2,#c9b49a 50%,#8a9fb3)"></div>
  <div class="band" style="background:var(--red)"><b>Learning</b><p>Structured lessons that match school ASL courses, with vocabulary lists and review drills after every unit.</p></div>
</div>
<div class="abs course" style="left:412px;top:1821px">
  <div class="tab" style="color:var(--blue)"><svg width="30" height="30"><circle cx="11" cy="10" r="5" fill="none" stroke="#999" stroke-width="2"/><circle cx="21" cy="14" r="4" fill="none" stroke="#999" stroke-width="2"/><path d="M2 28c0-7 4-10 9-10M16 28c0-5 2-8 5-8s6 3 6 8" fill="none" stroke="#999" stroke-width="2"/></svg>Parents</div>
  <div class="photo" role="img" aria-label="Photo of a parent signing with a young child" style="background:linear-gradient(135deg,#3b3b42,#6b6e78 60%,#2c2f3a)"></div>
  <div class="band" style="background:var(--blue)"><b>Hearing parents of deaf children</b><p>Signs for home routines, play and bedtime so the whole family can talk together from day one.</p></div>
</div>
<div class="abs course" style="left:824px;top:1821px">
  <div class="tab" style="color:var(--purple)"><svg width="34" height="30"><circle cx="9" cy="11" r="4" fill="none" stroke="#999" stroke-width="2"/><circle cx="17" cy="9" r="5" fill="none" stroke="#999" stroke-width="2"/><circle cx="25" cy="11" r="4" fill="none" stroke="#999" stroke-width="2"/><path d="M2 27c1-6 4-9 7-9M9 28c0-6 3-10 8-10s8 4 8 10M25 18c3 0 6 3 7 9" fill="none" stroke="#999" stroke-width="2"/></svg>Community</div>
  <div class="photo" role="img" aria-label="Photo of a smiling group of community members" style="background:linear-gradient(135deg,#c7c9cc,#a48a74 50%,#6e7d8c)"></div>
  <div class="band" style="background:var(--purple)"><b>Deaf and hard of hearing</b><p>Connect with coworkers, friends and neighbours through shared signs and community events.</p></div>
</div>

<h3 class="abs col-title" style="left:160px;top:2350px">—ASL Articles</h3>
<div class="abs" style="left:186px;top:2390px;width:390px">
  <div><span class="art-num">01</span> <span class="art-head">Choosing an American Sign Language Course</span></div>
  <p class="small" style="margin-top:14px;margin-left:34px">Congratulations! You have decided to learn Sign Language. Whether you are a parent, a friend or a coworker, learning to sign opens a new way to connect. Here is how to pick a course that fits your goals, your schedule and the way you like to learn best. More</p>
</div>
<div class="abs pager" style="left:220px;top:2562px"><span class="on"></span><span>2</span><span>3</span></div>

<h3 class="abs col-title" style="left:603px;top:2350px">—Frequently asked questions</h3>
<div class="abs faq" style="left:603px;top:2390px">
  <div class="q open" style="border:none">How do I subscribe to this website? <b>—</b></div>
  <p class="small" style="padding:10px 0 14px">American Sign Language is used by the Deaf community in many places. Choose a plan, create your account and start your first lesson right away.</p>
  <div class="q">How do I subscribe to this website? <b>+</b></div>
  <div class="q">Can I stop my subscription at any time? <b>+</b></div>
  <div class="q">What is the return policy? <b>+</b></div>
</div>

<section class="abs experts"><h4>MEET OUR DEAF EXPERTS</h4></section>
<div class="abs expert" style="left:500px;top:2771px"><div class="pic" role="img" aria-label="Portrait photo of an expert" style="background:linear-gradient(160deg,#c76a3b,#e9c9a8)"></div><div class="name">MARLA T.</div></div>
<div class="abs expert" style="left:816px;top:2771px"><div class="pic" role="img" aria-label="Portrait photo of an expert" style="background:linear-gradient(160deg,#3a3a3a,#7a6a5e)"></div><div class="name">NORA P.</div></div>
<svg class="abs" style="left:905px;top:2888px" width="46" height="46"><circle cx="23" cy="23" r="20" fill="none" stroke="#fff" stroke-width="2"/><path d="M23 13v20M13 23h20" stroke="#fff" stroke-width="2"/></svg>
<div class="abs expert" style="left:500px;top:3108px"><div class="pic" role="img" aria-label="Portrait photo of an expert" style="background:linear-gradient(160deg,#9db0a4,#d9d3c3)"></div><div class="name">IDA R.</div></div>
<div class="abs expert" style="left:816px;top:3108px"><div class="pic" role="img" aria-label="Portrait photo of an expert" style="background:linear-gradient(160deg,#6a4a3a,#b08870)"></div><div class="name">CALVIN O.</div></div>
<div class="abs" style="left:435px;top:3452px;width:765px;text-align:center;color:#fff;font-size:13px;font-weight:700;text-decoration:underline">See all members</div>

<div class="abs" style="left:26px;top:2860px;font-size:11px;font-weight:700">OUR FOUNDER</div>
<section class="abs founder">
  <div class="pic" role="img" aria-label="Portrait photo of the founder"></div>
  <div style="position:absolute;left:28px;top:296px;width:380px">
    <div style="color:var(--green);font-size:11px;font-weight:700;margin-bottom:10px">RUTH ALDER</div>
    <p class="small"><b>Founder</b> Ruth is a certified interpreter who has worked with deaf children for over fifteen years. She has taught sign language in schools, colleges and at home, and has mentored many new interpreters. After launching a video program in 2006, she turned it into this online course so anyone can learn ASL from home. Ruth believes clear signing opens doors and every learner can reach full potential.</p>
  </div>
</section>

<footer class="abs footer">
  <div class="abs fcol" style="left:160px;top:56px"><h5>Navigation</h5><ul><li>Home</li><li>About us</li><li>Buy now</li><li>Course plan</li><li>Group rate form</li><li>Teachers guide</li></ul></div>
  <div class="abs fcol" style="left:330px;top:56px"><h5>About us</h5><ul><li>How it works</li><li>Video testimonials</li><li>Gift certificates</li><li>Foundraising your ASL program</li><li>Blog</li></ul></div>
  <div class="abs" style="left:628px;top:56px">
    <div style="font-size:14px;font-weight:700;margin-bottom:12px">Newsletter Subscription</div>
    <div class="signup"><span>E-mail address</span><i><svg width="18" height="16"><path d="M1 8L17 1 12 15 9 9z" fill="#fff"/></svg></i></div>
    <div style="font-size:12px;font-weight:700;margin:14px 0 10px">Connect with us through</div>
    <div class="socials"><span></span><span></span><span></span><span></span></div>
  </div>
</footer>

<div class="abs copy">Copyright © 2017. Designer by HandwiseLessons. All Rights Reserved.</div>

</body>
</html>
```